Dale Winslow Drum Demo

My husband and I just moved to Nashville. Dale (my husband) is a drummer with 30 years of experience. We have a CD that we would like to promote with hope that he can get a gig doing what he loves. We would like your talented artists to create a CD cover and label. We are here to promote Dale, although we also think the rest of the band should be mentioned and recognized. I am going to put the names of the musicians as well as two pictures that can be used for the outside cover if necessary. On the inside of the cover I would like the band members mentioned as well as a little bio. about Dale.
Dale Winslow - drums and vocals
Mark Delvey - vocals
Rick Hanlon - bass
Pete Morant - lead guitar

Dale's bio
Born in Massachusetts
30 years experience
some drumming school
local band experience
music played: blues, classic rock, country, jazz, and alternative
influences: Carl Mesner, Lenny Vask, Glen Fosk, Walt Dusek
Great passion, feel, and desire for music....something which cannot be taught!!!

```html
<!DOCTYPE html>
<html lang="en">
<head>
<meta charset="utf-8">
<title>Dale Winslow Demo – CD Artwork</title>
<link href="https://fonts.googleapis.com/css2?family=Oswald:wght@500&family=Pathway+Gothic+One&display=swap" rel="stylesheet">
<style>
  :root {
    --page-bg: #e4e2e3;
    --steel-light: #8a8986;
    --steel-mid: #5c5b58;
    --steel-dark: #2a2928;
    --tray-bg: #231a1c;
    --tray-glow: #3a2c2b;
    --title-white: #f1efea;
    --body-text: #d9d2cc;
    --divider: #8a7b72;
  }
  * { box-sizing: border-box; margin: 0; padding: 0; }
  html, body { width: 1200px; height: 900px; overflow: hidden; }
  body {
    background: var(--page-bg);
    position: relative;
    font-family: "Pathway Gothic One", "Arial Narrow", sans-serif;
  }

  .cover-title {
    position: absolute;
    left: 0; right: 0; top: 50%;
    transform: translateY(-50%);
    font-family: "Oswald", "Arial Narrow", sans-serif;
    font-weight: 500;
    color: var(--title-white);
    text-transform: uppercase;
    text-align: center;
    line-height: 0.98;
    letter-spacing: -1px;
    text-shadow: 0 3px 8px rgba(0,0,0,0.45);
  }

  /* Front cover */
  .front-cover {
    position: absolute;
    left: 170px; top: 30px;
    width: 360px; height: 360px;
    overflow: hidden;
    box-shadow: 0 8px 24px rgba(0,0,0,0.25);
  }
  .front-photo {
    position: absolute; inset: 0;
    background: radial-gradient(circle at 50% 50%, var(--steel-light) 0%, var(--steel-mid) 48%, var(--steel-dark) 100%);
  }
  .front-cover .cover-title { font-size: 82px; }

  /* Disc label */
  .disc-label {
    position: absolute;
    left: 670px; top: 30px;
    width: 360px; height: 360px;
    border-radius: 50%;
    overflow: hidden;
    box-shadow: 0 8px 24px rgba(0,0,0,0.25);
  }
  .disc-photo {
    position: absolute; inset: 0;
    background: radial-gradient(circle at 50% 50%, var(--steel-light) 0%, var(--steel-mid) 50%, var(--steel-dark) 100%);
  }
  .disc-label .cover-title { font-size: 78px; }
  .disc-hub {
    position: absolute;
    left: 50%; top: 50%;
    width: 100px; height: 100px;
    transform: translate(-50%, -50%);
    border-radius: 50%;
    background: rgba(59,58,57,0.85);
    border: 2px solid #55534f;
  }
  .disc-hole {
    position: absolute;
    left: 50%; top: 50%;
    width: 36px; height: 36px;
    transform: translate(-50%, -50%);
    border-radius: 50%;
    background: var(--page-bg);
  }

  /* Back tray card */
  .tray-card {
    position: absolute;
    left: 330px; top: 425px;
    width: 540px; height: 445px;
    background: linear-gradient(180deg, var(--tray-glow) 0%, var(--tray-bg) 100%);
    overflow: hidden;
    box-shadow: 0 8px 24px rgba(0,0,0,0.25);
    color: var(--body-text);
  }
  .kit-photo {
    position: absolute;
    left: 255px; top: 18px;
    width: 268px; height: 250px;
    background: radial-gradient(ellipse at 50% 50%, #a08a6c 0%, #5b4a3d 40%, var(--tray-bg) 75%);
  }
  .band-list {
    position: absolute;
    left: 24px; top: 26px;
    list-style: none;
    font-size: 15px;
    line-height: 1.55;
  }
  .band-list li { display: flex; }
  .member-name {
    width: 100px;
    text-align: right;
    padding-right: 8px;
    border-right: 1px solid var(--divider);
    color: var(--title-white);
  }
  .member-role { padding-left: 8px; }
  .bio {
    position: absolute;
    left: 24px; top: 284px;
    width: 496px;
    font-size: 14px;
    line-height: 1.3;
  }
  .bio strong { color: var(--title-white); font-weight: 400; }
  .bio p + p { margin-top: 2px; }
  .bio-facts { margin-bottom: 8px; }
</style>
</head>
<body>

  <section class="front-cover">
    <div class="front-photo" role="img" aria-label="Close-up photo of a worn drum head with two crossed wooden drumsticks"></div>
    <h1 class="cover-title">Dale<br>Winslow<br>Demo</h1>
  </section>

  <section class="disc-label">
    <div class="disc-photo" role="img" aria-label="Drum head photo with crossed drumsticks printed across the disc"></div>
    <div class="cover-title">Dale<br>Winslow<br>Demo</div>
    <div class="disc-hub"></div>
    <div class="disc-hole"></div>
  </section>

  <section class="tray-card">
    <div class="kit-photo" role="img" aria-label="Photo of a drum kit with cymbals on a dark stage"></div>

    <ul class="band-list">
      <li><span class="member-name">Dale Winslow</span><span class="member-role">Drums and vocals</span></li>
      <li><span class="member-name">Mark Delvey</span><span class="member-role">Vocals</span></li>
      <li><span class="member-name">Rick Hanlon</span><span class="member-role">Bass</span></li>
      <li><span class="member-name">Pete Morant</span><span class="member-role">Lead guitar</span></li>
    </ul>

    <div class="bio">
      <div class="bio-facts">
        <p><strong>Dale Winslow</strong>, Born in Massachusetts,</p>
        <p>30 years experience</p>
        <p>some drumming school</p>
        <p>local band experience</p>
      </div>
      <p><strong>Music played:</strong> blues, classic rock, country, jazz, and alternative</p>
      <p><strong>Influences:</strong> Carl Mesner, Lenny Vask, Glen Fosk, Walt Dusek</p>
      <p>Great passion, feel, and desire for music... something which cannot be taught!</p>
    </div>
  </section>

</body>
</html>
```